drafting business needs a 2 sided rack card design. Size specificaton

Document Trim Size:
Full Bleed Size (starting document size)
3.86" x 8.39"
When trimmed the Rack cards are 3.74" x 8.27".
300 DPI

I need my logo, product info, and 2 pictures included

This is product information that i need:

- Floor Plans measured to KEDV & TRUZ standards
- Stunning HD Photography
- Vistaloom - your space delivered in perfect 3D
- E &O insured
- Our products delivered next by before 10:00 AM

It also has to my my special offer: Save 50% off Vistaloom, Floor Plans, and Photography

My contact info is
www.tidewellplans-demo.com
dorian@tidewellplans-demo.com
555-014-2286

Hey designers, the common element I see in most of the designs that I actually don't like is the use of orange and blue. I think there was some miscommunication. Please Don't use these colors. It really makes the designs Look cheap. I want a clean, high end look.

realtors

Real Estate

Serif

• At least 2 photos and my logo included. it must include all my wording with discount in bold, but classy.
• I want clean classy design. My logo is and 2 photos should be in design. I design should match my logo colors, I think. I have tons of other photos if you think these arent very useful
• Also I have attached a logo from vistaloom. Please include this, but smaller than the Tidewell Plans. The Vistaloom is just equiptment that I use
• This is a discount promotion, but I dont want it to look cheap whatsoever

```html
<!DOCTYPE html>
<html lang="en">
<head>
<meta charset="utf-8">
<title>Tidewell Plans Rack Card</title>
<link rel="stylesheet" href="https://fonts.googleapis.com/css2?family=Jost:wght@400;500&family=Oswald:wght@500;600&family=Pathway+Gothic+One&display=swap">
<style>
  :root{
    --gold:#a8875a;
    --gold-deep:#8c6d43;
    --charcoal:#2e3133;
    --ink:#3a3a3a;
    --paper:#ffffff;
    --mist:#efede9;
    --stage:#2b2b2b;
  }
  *{margin:0;padding:0;box-sizing:border-box}
  html,body{width:960px;height:1200px;overflow:hidden;background:var(--stage)}
  .canvas{position:relative;width:960px;height:1200px}
  .card{position:absolute;top:148px;width:410px;height:904px;background:var(--paper);overflow:hidden}
  .card--front{left:55px}
  .card--back{left:496px}

  .photo{position:absolute}
  .photo--dining{left:0;top:0;width:410px;height:660px;
    background:linear-gradient(180deg,#d6d5d3 0%,#a9a7a3 45%,#6b4a33 70%,#8a6f5a 100%)}
  .photo--hall{left:0;top:0;width:205px;height:320px;
    background:linear-gradient(160deg,#e9e6df 0%,#cfc7b8 50%,#8a5330 100%)}
  .photo--living{left:213px;top:0;width:197px;height:152px;
    background:linear-gradient(180deg,#e4e6e8 0%,#c9c6c0 60%,#6e5a48 100%)}
  .photo--bedroom{left:213px;top:162px;width:197px;height:158px;
    background:linear-gradient(180deg,#ccc6c2 0%,#b6aaa5 50%,#e8dcd9 100%)}

  .offer-badge{position:absolute;left:110px;top:-88px;width:344px;height:344px;border-radius:50%;background:var(--charcoal)}
  .offer{position:absolute;display:flex;align-items:center;color:var(--paper)}
  .offer__save{font-family:'Oswald',sans-serif;font-weight:500;writing-mode:vertical-rl;transform:rotate(180deg);line-height:1}
  .offer__num{font-family:'Oswald',sans-serif;font-weight:600;line-height:.8}
  .offer__pct{display:flex;flex-direction:column;font-family:'Oswald',sans-serif;font-weight:600;line-height:.9}
  .offer__pct span:first-child{font-weight:500}
  .offer--front{left:150px;top:26px}
  .offer--front .offer__save{font-size:38px;margin-right:4px}
  .offer--front .offer__num{font-size:124px}
  .offer--front .offer__pct{font-size:48px;margin-left:4px}
  .offer-lines{position:absolute;font-family:'Jost',sans-serif;font-weight:500;color:var(--paper);text-transform:uppercase}
  .offer-lines--front{right:24px;top:136px;text-align:right;font-size:22px;line-height:29px}

  .vistaloom{position:absolute;left:16px;top:16px;display:flex;align-items:center;gap:6px;padding:4px 9px;background:var(--paper);font-family:'Jost',sans-serif;font-weight:500;font-size:13px;color:var(--charcoal);letter-spacing:.5px}
  .vistaloom::before{content:"";width:8px;height:8px;background:var(--gold)}

  .band{position:absolute;left:0;top:328px;width:410px;height:108px;background:var(--charcoal)}
  .offer--back{left:16px;top:350px}
  .offer--back .offer__save{font-size:30px;margin-right:3px}
  .offer--back .offer__num{font-size:86px}
  .offer--back .offer__pct{font-size:34px;margin-left:2px}
  .offer-lines--back{left:196px;top:344px;font-size:20px;line-height:25px}

  .brand{position:absolute;left:0;top:596px;width:410px;text-align:center}
  .brand__mark{display:block;margin:0 auto;width:108px;height:108px;border-radius:50%;background:var(--paper);border:6px solid var(--paper);box-shadow:0 0 0 2px #e3ddd3 inset}
  .brand__name{display:block;margin-top:4px;font-family:'Jost',sans-serif;font-weight:400;font-size:34px;color:var(--charcoal)}

  .contact{position:absolute;left:25px;top:766px;width:360px;height:112px;border-radius:16px;overflow:hidden;background:var(--paper);box-shadow:0 6px 10px rgba(0,0,0,.12)}
  .contact__head{height:42px;display:flex;align-items:center;justify-content:center;font-family:'Jost',sans-serif;font-size:25px;color:var(--paper);text-transform:uppercase}
  .contact__phone{height:70px;display:flex;align-items:center;justify-content:center;font-family:'Pathway Gothic One',sans-serif;font-size:64px;line-height:1}
  .contact--front{border:2px solid var(--charcoal)}
  .contact--front .contact__head{background:var(--charcoal)}
  .contact--front .contact__phone{color:var(--gold-deep)}
  .contact--back{left:24px;border:2px solid var(--gold)}
  .contact--back .contact__head{background:var(--gold)}
  .contact--back .contact__phone{color:var(--charcoal)}

  .features{position:absolute;left:30px;top:462px;list-style:none;font-family:'Pathway Gothic One',sans-serif;font-size:22px;color:var(--ink);line-height:30px}
  .features li{display:flex;align-items:center}
  .features svg{width:16px;height:16px;margin-right:9px;flex:none}
  .features .accent{color:var(--gold-deep)}

  .consult{position:absolute;left:0;top:634px;width:410px;height:120px;background:var(--mist);text-align:center}
  .consult__title{font-family:'Oswald',sans-serif;font-weight:500;font-size:40px;color:var(--charcoal);line-height:1;margin-top:14px;letter-spacing:.5px}
  .consult__line{display:flex;align-items:center;justify-content:center;font-family:'Jost',sans-serif;font-size:21px;color:var(--ink);line-height:30px}
  .consult__line svg{width:14px;height:14px;margin-right:8px}
</style>
</head>
<body>
<div class="canvas">

  <section class="card card--front">
    <div class="photo photo--dining" role="img" aria-label="Bright dining room with a polished wood table, chairs and tall windows"></div>
    <div class="vistaloom">Vistaloom</div>
    <div class="offer-badge"></div>
    <div class="offer offer--front">
      <span class="offer__save">SAVE</span>
      <span class="offer__num">50</span>
      <span class="offer__pct"><span>%</span><span>OFF</span></span>
    </div>
    <p class="offer-lines offer-lines--front">On Vistaloom,<br>Floor plans, and<br>Photography</p>
    <div class="brand">
      <span class="brand__mark"></span>
      <span class="brand__name">Tidewell Plans</span>
    </div>
    <div class="contact contact--front">
      <div class="contact__head">Contact us today</div>
      <div class="contact__phone">555-014-2286</div>
    </div>
  </section>

  <section class="card card--back">
    <div class="photo photo--hall" role="img" aria-label="Entry hall with tiled floor, wooden staircase and a framed landscape painting"></div>
    <div class="photo photo--living" role="img" aria-label="Living room with white sofas, rug and large windows"></div>
    <div class="photo photo--bedroom" role="img" aria-label="Bedroom with dark headboard, lamps and a round mirror"></div>
    <div class="band"></div>
    <div class="offer offer--back">
      <span class="offer__save">SAVE</span>
      <span class="offer__num">50</span>
      <span class="offer__pct"><span>%</span><span>OFF</span></span>
    </div>
    <p class="offer-lines offer-lines--back">On Vistaloom,<br>Floor plans, and<br>Photography</p>

    <ul class="features">
      <li><svg viewBox="0 0 16 16"><path d="M2 8.5l4 4 8-9" fill="none" stroke="#a8875a" stroke-width="2"/></svg>Floor Plans measured to KEDV &amp; TRUZ standards</li>
      <li><svg viewBox="0 0 16 16"><path d="M2 8.5l4 4 8-9" fill="none" stroke="#a8875a" stroke-width="2"/></svg>Stunning HD Photography</li>
      <li><svg viewBox="0 0 16 16"><path d="M2 8.5l4 4 8-9" fill="none" stroke="#a8875a" stroke-width="2"/></svg>Vistaloom - your space delivered in perfect 3D</li>
      <li><svg viewBox="0 0 16 16"><path d="M2 8.5l4 4 8-9" fill="none" stroke="#a8875a" stroke-width="2"/></svg>E &amp;O insured</li>
      <li><svg viewBox="0 0 16 16"><path d="M2 8.5l4 4 8-9" fill="none" stroke="#a8875a" stroke-width="2"/></svg>Our products delivered next by before&nbsp;<span class="accent">10:00 AM</span></li>
    </ul>

    <div class="consult">
      <h2 class="consult__title">FREE CONSULTATION</h2>
      <p class="consult__line"><svg viewBox="0 0 14 14"><circle cx="7" cy="7" r="6" fill="none" stroke="#a8875a" stroke-width="1.4"/><path d="M1 7h12M7 1c-3 3-3 9 0 12M7 1c3 3 3 9 0 12" fill="none" stroke="#a8875a" stroke-width="1.2"/></svg>www.tidewellplans-demo.com</p>
      <p class="consult__line"><svg viewBox="0 0 14 14"><rect x="1" y="3" width="12" height="8" fill="#a8875a"/><path d="M1 3l6 5 6-5" fill="none" stroke="#fff" stroke-width="1.2"/></svg>dorian@tidewellplans-demo.com</p>
    </div>

    <div class="contact contact--back">
      <div class="contact__head">Contact us today</div>
      <div class="contact__phone">555-014-2286</div>
    </div>
  </section>

</div>
</body>
</html>
```